Academy Values Classroom Poster

Marrowdene Community Academy has the core values of Aspiration, Positivity, Responsibility and Achievement at its heart. We have these words displayed in our entrance (in Bliss font) but would like them to permeate into the classroom spaces in a poster form. We want a clear message that shows what the values mean to students:

Aspiration - Think BIG (pantone 717)
Positivity - Smile :-) (pantone 376)
Responsibility - for yourself and others (pantone 569)
Achievement - Celebrate Success! (pantone 214)

It would be good to follow the colour scheme of the main words to create a 'brand' for these values (pantone refs noted in brackets) and we would like to see some clean designs please.

I anticipate these will be A1 posters.

I have attached our school logo although it is not essential that this is included.

Target Market(s)

Students

Industry/Entity Type

School

Font styles to use
Other font styles liked:
• Bliss or Segoe UI

Requirements
Must have
• Aspiration - Think BIG
Positivity - Smile :-)
Responsibility - for yourself and others
Achievement - Celebrate Success!
Should not have
• Nothing too busy

```html
<!DOCTYPE html>
<html lang="en">
<head>
<meta charset="utf-8">
<title>Marrowdene Community Academy – Our Values</title>
<link rel="stylesheet" href="https://fonts.googleapis.com/css2?family=Graduate&family=Open+Sans:wght@600&display=swap">
<style>
  :root {
    --board-dark: #262626;
    --board-mid: #3d3d3d;
    --board-light: #4d4d4d;
    --chalk-white: #d9d9d9;
    --aspiration: #f28a2e;
    --positivity: #5cb947;
    --responsibility: #3fbf9d;
    --achievement: #e0197c;
    --crest-block: #6f7a80;
  }
  * { margin: 0; padding: 0; box-sizing: border-box; }
  html, body { width: 847px; height: 1200px; overflow: hidden; background: var(--board-dark); }
  .poster {
    position: relative;
    width: 847px;
    height: 1200px;
    overflow: hidden;
    background: radial-gradient(ellipse at 45% 45%, var(--board-light) 0%, var(--board-mid) 50%, var(--board-dark) 100%);
    font-family: "Graduate", Georgia, serif;
  }

  .brand {
    position: absolute;
    left: 206px;
    top: 66px;
    display: flex;
    align-items: center;
    gap: 22px;
  }
  .brand-mark {
    width: 104px;
    height: 104px;
    background: var(--crest-block);
  }
  .brand-name {
    font-family: "Open Sans", Arial, sans-serif;
    font-weight: 600;
    color: var(--chalk-white);
    line-height: 1.05;
  }
  .brand-name .line-main { display: block; font-size: 52px; letter-spacing: -0.5px; }
  .brand-name .line-sub { display: block; font-size: 25px; }

  .value-line {
    position: absolute;
    left: 0;
    width: 847px;
    text-align: center;
    text-transform: uppercase;
    white-space: nowrap;
    line-height: 1;
  }
  .word { font-size: 60px; letter-spacing: -0.5px; }
  .meaning { font-size: 50px; letter-spacing: -1.5px; }
  .meaning--own-line { letter-spacing: -0.5px; }

  .aspiration { color: var(--aspiration); }
  .positivity { color: var(--positivity); }
  .responsibility { color: var(--responsibility); }
  .achievement { color: var(--achievement); }

  .line-aspiration { top: 327px; }
  .line-positivity { top: 458px; }
  .line-responsibility { top: 601px; }
  .line-responsibility-meaning { top: 682px; }
  .line-achievement { top: 820px; }
  .line-achievement-meaning { top: 894px; }
</style>
</head>
<body>
  <main class="poster">
    <header class="brand">
      <div class="brand-mark"></div>
      <div class="brand-name">
        <span class="line-main">Marrowdene</span>
        <span class="line-sub">Community Academy</span>
      </div>
    </header>

    <p class="value-line line-aspiration aspiration">
      <span class="word">Aspiration</span> <span class="meaning">- Think Big</span>
    </p>

    <p class="value-line line-positivity positivity">
      <span class="word">Positivity</span> <span class="meaning">- Smile :-)</span>
    </p>

    <p class="value-line line-responsibility responsibility">
      <span class="word">Responsibility</span>
    </p>
    <p class="value-line line-responsibility-meaning responsibility">
      <span class="meaning meaning--own-line">- For yourself and others</span>
    </p>

    <p class="value-line line-achievement achievement">
      <span class="word">Achievement</span>
    </p>
    <p class="value-line line-achievement-meaning achievement">
      <span class="meaning meaning--own-line">- Celebrate Success !</span>
    </p>
  </main>
</body>
</html>
```